WE HAND MAKE AND DECORATE BEAUTIFUL CREATIVE GINGER BREAD HOUSES FOR CHRISTMAS AND CUPCAKES FOR SPECIAL OCCASIONS

Contact Information for Business Card

MAPLE AND THISTLE DESIGNS
FLORA 0467 213 809
BRENDA 0455038216

```html
<!DOCTYPE html>
<html lang="en">
<head>
<meta charset="utf-8">
<title>Maple and Thistle Designs – Business Card</title>
<link href="https://fonts.googleapis.com/css2?family=Mystery+Quest&family=Roboto+Condensed:wght@300;400&display=swap" rel="stylesheet">
<style>
  :root {
    --plank-light: #f6f3f8;
    --plank-mid: #e9e3ee;
    --plank-line: #d9cfe2;
    --lavender-tint: rgba(196, 170, 230, 0.28);
    --brand-purple: #8a2fd6;
    --body-brown: #6b4535;
    --photo-warm: #b89a86;
    --photo-pink: #d8a9c3;
    --photo-dark: #6e4a45;
  }
  * { margin: 0; padding: 0; box-sizing: border-box; }
  html, body { width: 1200px; height: 741px; overflow: hidden; background: #fff; }
  .card {
    position: relative;
    width: 1200px;
    height: 741px;
    overflow: hidden;
    background:
      linear-gradient(100deg, transparent 40%, var(--lavender-tint) 70%, transparent 95%),
      repeating-linear-gradient(180deg,
        var(--plank-light) 0px, var(--plank-light) 40px,
        var(--plank-mid) 40px, var(--plank-mid) 52px,
        var(--plank-line) 52px, var(--plank-line) 54px);
  }
  .house-photo {
    position: absolute;
    left: 0; top: 0;
    width: 620px; height: 741px;
    background:
      radial-gradient(ellipse at 40% 25%, var(--photo-dark) 0%, transparent 45%),
      radial-gradient(ellipse at 20% 60%, var(--photo-pink) 0%, transparent 40%),
      linear-gradient(160deg, var(--photo-warm) 0%, #c9b3a6 55%, #e8dde0 100%);
    -webkit-mask-image: linear-gradient(90deg, #000 55%, transparent 100%);
    mask-image: linear-gradient(90deg, #000 55%, transparent 100%);
    opacity: 0.85;
  }
  .brand {
    position: absolute;
    right: 87px;
    top: 36px;
    text-align: right;
    font-family: "Mystery Quest", cursive;
    font-weight: 400;
    color: var(--brand-purple);
    font-size: 82px;
    line-height: 108px;
  }
  .brand-mark {
    position: absolute;
    left: 392px;
    top: 50px;
    width: 90px; height: 90px;
    border-radius: 50%;
    background: var(--brand-purple);
  }
  .tagline {
    position: absolute;
    right: 70px;
    top: 278px;
    width: 600px;
    text-align: right;
    font-family: "Roboto Condensed", sans-serif;
    font-weight: 400;
    font-size: 37px;
    line-height: 46px;
    color: var(--body-brown);
  }
  .contacts {
    position: absolute;
    right: 75px;
    top: 515px;
    list-style: none;
    font-family: "Mystery Quest", cursive;
    color: var(--brand-purple);
    font-size: 52px;
  }
  .contact {
    display: flex;
    align-items: center;
    justify-content: flex-end;
    height: 80px;
  }
  .contact:nth-child(2) { margin-right: 12px; }
  .contact svg { width: 34px; height: 60px; margin-right: 18px; }
</style>
</head>
<body>
  <main class="card">
    <div class="house-photo" role="img" aria-label="Photo of a decorated gingerbread house with candy canes and icing"></div>

    <span class="brand-mark" aria-hidden="true"></span>
    <h1 class="brand">Maple and Thistle<br>Designs</h1>

    <p class="tagline">We hand make and decorate beautiful,<br>creative gingerbread houses for<br>Christmas and cupcakes for<br>special occasions.</p>

    <ul class="contacts">
      <li class="contact">
        <svg viewBox="0 0 34 60" aria-hidden="true"><path d="M17 58 C17 58 3 32 3 18 a14 14 0 0 1 28 0 C31 32 17 58 17 58 Z" fill="none" stroke="currentColor" stroke-width="3"/><circle cx="17" cy="18" r="6" fill="none" stroke="currentColor" stroke-width="3"/></svg>
        <span>Flora 0467 213 809</span>
      </li>
      <li class="contact">
        <svg viewBox="0 0 34 60" aria-hidden="true"><path d="M17 58 C17 58 3 32 3 18 a14 14 0 0 1 28 0 C31 32 17 58 17 58 Z" fill="none" stroke="currentColor" stroke-width="3"/><circle cx="17" cy="18" r="6" fill="none" stroke="currentColor" stroke-width="3"/></svg>
        <span>Brenda 0455038216</span>
      </li>
    </ul>
  </main>
</body>
</html>
```